Newsletter the first sustainable shin guards are here. Play sustainably

We would like to advertise our Kelvora shin guards with a newsletter for the first time. Our articles should be presented and something should be told about our product.

Kelvra is the first shin guard made entirely from sustainable materials. The patented process from Swiss production not only guarantees fantastic stability on the football field, but also protects the environment.

Further information at www.kelvora-sample.ch

Target Market(s)

Private individuals and clubs who would like to have our schooner with their logo in their shop

Requirements
Must have
• Buttons with the products to buy them straight away
Nice to have
• everything on www.kelvora-sample.ch

```html
<!DOCTYPE html>
<html lang="de">
<head>
<meta charset="utf-8">
<title>Kelvora Newsletter</title>
<link href="https://fonts.googleapis.com/css2?family=Roboto:wght@400;500;700;900&display=swap" rel="stylesheet">
<style>
  :root {
    --bg-dark: #2a2a2a;
    --bg-mid: #3a3a3a;
    --bg-footer: #222222;
    --teal: #2db5a5;
    --teal-hero: #559a92;
    --card: #6b6b6b;
    --wood-light: #e2bb8c;
    --wood: #c99560;
    --white: #ffffff;
  }
  * { margin: 0; padding: 0; box-sizing: border-box; }
  html, body { width: 1200px; height: 3650px; overflow: hidden; background: var(--bg-dark); }
  body { font-family: "Roboto", Arial, sans-serif; color: var(--white); }
  section, header, footer { position: absolute; left: 0; width: 1200px; }
  .abs { position: absolute; }

  .brand {
    font-family: "Roboto", Arial, sans-serif;
    font-weight: 900;
    color: var(--white);
    letter-spacing: -1px;
    line-height: 1;
    text-align: center;
    width: 100%;
  }

  .site-header { top: 0; height: 188px; background: var(--bg-dark); }
  .site-header .brand { top: 30px; font-size: 128px; }

  .hero { top: 188px; height: 675px; background: var(--teal-hero); }
  .hero-photo { left: 150px; top: 52px; width: 420px; height: 623px;
    background: linear-gradient(180deg, #e9c9a8 0%, #d8a986 35%, #2f4a6c 60%, #263c5a 100%);
    border-radius: 200px 200px 0 0; }
  .hero-title { left: 653px; top: 175px; font-size: 92px; font-weight: 900; }
  .hero-text { left: 657px; top: 325px; width: 460px; font-size: 30px; line-height: 48px; }

  .products { top: 863px; height: 889px; background: var(--bg-dark); }
  .section-title { font-size: 51px; font-weight: 700; }
  .products .section-title { top: 110px; width: 100%; text-align: center; }
  .product-card { top: 208px; width: 320px; text-align: center; }
  .product-image { width: 320px; height: 333px;
    background:
      radial-gradient(ellipse 22% 42% at 50% 52%, var(--wood-light) 0%, var(--wood) 55%, rgba(201,149,96,0) 100%),
      var(--card); }
  .product-price { margin-top: 28px; font-size: 37px; font-weight: 700; color: var(--teal); }
  .product-name { margin-top: 10px; font-size: 28px; font-weight: 700; text-transform: uppercase; }
  .btn {
    display: inline-block; width: 216px; height: 81px; line-height: 77px;
    border: 3px solid var(--teal); color: var(--teal);
    font-size: 27px; font-weight: 700; text-align: center; text-decoration: none;
  }
  .product-card .btn { margin-top: 30px; }

  .story { top: 1752px; height: 675px; background: var(--bg-mid); }
  .story .section-title { left: 144px; top: 120px; }
  .story-text { left: 146px; top: 220px; width: 340px; font-size: 30px; line-height: 48px; }
  .story .btn { left: 146px; top: 464px; }
  .story-photo { left: 573px; top: 108px; width: 482px; height: 462px;
    border: 7px solid var(--teal);
    background: linear-gradient(160deg, #c8202a 0%, #b51c22 30%, #a9a9a9 45%, #c9c2b6 70%, #d9b98e 100%); }

  .players { top: 2427px; height: 768px; background: var(--bg-dark); }
  .players-photo { left: 75px; top: 93px; width: 480px; height: 593px;
    border-radius: 240px;
    background: linear-gradient(180deg, #2aa99a 0%, #2db5a5 30%, #d83a2e 60%, #c9302a 100%); }
  .players .section-title { left: 683px; top: 190px; }
  .players-text { left: 683px; top: 290px; width: 420px; font-size: 30px; line-height: 48px; }
  .players .btn { left: 683px; top: 498px; }

  .site-footer { top: 3195px; height: 455px; background: var(--bg-footer); }
  .site-footer .brand { top: 85px; font-size: 128px; }
  .social { left: 560px; top: 245px; width: 81px; height: 81px; border-radius: 50%; background: var(--teal); }
  .copyright { top: 358px; width: 100%; text-align: center; font-size: 24px; }
</style>
</head>
<body>
  <header class="site-header">
    <div class="brand abs">kelvora</div>
  </header>

  <section class="hero">
    <div class="hero-photo abs" role="img" aria-label="Foto: Spielerin im blauen Trikot hält zwei personalisierte Holz-Schienbeinschoner"></div>
    <h1 class="hero-title abs">Products</h1>
    <p class="hero-text abs">Design your shin guards completely according to your taste.</p>
  </section>

  <section class="products">
    <h2 class="section-title abs">Our Product</h2>
    <div class="product-card abs" style="left:72px">
      <div class="product-image" role="img" aria-label="Produktfoto: Holz-Schienbeinschoner mit eigenem Logo"></div>
      <div class="product-price">CHF 79.00</div>
      <div class="product-name">Personalisierbar</div>
      <a class="btn" href="#">BUY NOW</a>
    </div>
    <div class="product-card abs" style="left:441px">
      <div class="product-image" role="img" aria-label="Produktfoto: Holz-Schienbeinschoner Kelvora"></div>
      <div class="product-price">CHF 49.00</div>
      <div class="product-name">Kelvora</div>
      <a class="btn" href="#">BUY NOW</a>
    </div>
    <div class="product-card abs" style="left:810px">
      <div class="product-image" role="img" aria-label="Produktfoto: Holz-Schienbeinschoner im Vereinsdesign FC Lindenau"></div>
      <div class="product-price">CHF 49.00</div>
      <div class="product-name">FC Lindenau</div>
      <a class="btn" href="#">BUY NOW</a>
    </div>
  </section>

  <section class="story">
    <h2 class="section-title abs">Story</h2>
    <p class="story-text abs">Der erste ökologische Schienbeinschoner aus patentierter Schweizer Produktion.</p>
    <a class="btn abs" href="#">BUY NOW</a>
    <div class="story-photo abs" role="img" aria-label="Foto: Schienbeinschoner aus Holz wird in der Produktion bedruckt"></div>
  </section>

  <section class="players">
    <div class="players-photo abs" role="img" aria-label="Foto: Spieler im roten Trikot hält einen Holz-Schienbeinschoner"></div>
    <h2 class="section-title abs">Players</h2>
    <p class="players-text abs">Die Kelvora-Ambassadors haben ihren Lieblingsschoner persönlich gestaltet.</p>
    <a class="btn abs" href="#">BUY NOW</a>
  </section>

  <footer class="site-footer">
    <div class="brand abs">kelvora</div>
    <a class="social abs" href="#" aria-label="Social Media"></a>
    <p class="copyright abs">©Copyrights 2023 Kelvora &nbsp;|&nbsp;&nbsp; All Rights Reserved</p>
  </footer>
</body>
</html>
```